Fish guide business card

Buisiness card

Target Market(s)

Visitors to Campbell River Bc wanting to catch fish in the ocean and have a memorable adventure fun filled day

Industry/Entity Type

Tourism

Contact Information for Business Card

Phone number 250 318 two cards Ray 250 318 7262 other card Lou 250 6093714 both have email info@lwgullrocktours.com and website www.lwgullrocktours.com

Requirements
Must have
• Email, website , name , phone , logo , Campbell River BC
Nice to have
• Uploaded pictures have boat and man with fish picture

```html
<!DOCTYPE html>
<html lang="en">
<head>
<meta charset="utf-8">
<title>LW Gull Rock Tours – Business Card</title>
<link href="https://fonts.googleapis.com/css2?family=Montserrat:wght@600;700&display=swap" rel="stylesheet">
<style>
  :root {
    --navy: #262262;
    --teal: #00a9c5;
    --white: #ffffff;
    --photo-dark: #3f3c86;
    --photo-light: #7a78b8;
    --page: #86878b;
  }
  * { margin: 0; padding: 0; box-sizing: border-box; }
  html, body { width: 1200px; height: 1000px; overflow: hidden; }
  body {
    background: var(--page);
    font-family: "Montserrat", Arial, sans-serif;
    position: relative;
  }
  .card {
    position: absolute;
    left: 293px;
    width: 615px;
    height: 351px;
    overflow: hidden;
  }
  .card--front { top: 87px; background: var(--navy); }
  .card--back { top: 511px; background: var(--white); }
  .card__art { position: absolute; inset: 0; }

  .brand-seal {
    position: absolute;
    display: flex;
    align-items: center;
    justify-content: center;
    text-align: center;
    border-radius: 50%;
    background: var(--white);
    color: var(--navy);
    font-weight: 700;
    line-height: 1.15;
  }
  .card--front .brand-seal {
    left: 202px; top: 71px; width: 212px; height: 212px;
    border: 8px solid var(--navy);
    box-shadow: 0 0 0 3px var(--white);
    font-size: 24px;
  }
  .card--back .brand-seal {
    left: 113px; top: 17px; width: 158px; height: 158px;
    border: 6px solid var(--navy);
    font-size: 18px;
  }
  .website {
    position: absolute;
    left: 0; right: 0; top: 306px;
    display: flex; justify-content: center; align-items: center; gap: 5px;
    color: var(--white);
    font-weight: 700;
    font-size: 16px;
  }
  .person-name {
    position: absolute;
    left: 85px; top: 194px;
    color: var(--teal);
    font-weight: 700;
    font-size: 28px;
  }
  .contact-list {
    position: absolute;
    left: 87px; top: 247px;
    list-style: none;
    color: var(--navy);
    font-weight: 700;
    font-size: 15.5px;
  }
  .contact-list li {
    display: flex; align-items: center; gap: 11px;
    height: 24.5px;
  }
  .contact-list svg { width: 15px; height: 17px; flex: none; }
</style>
</head>
<body>

<section class="card card--front">
  <svg class="card__art" viewBox="0 0 615 351" aria-hidden="true">
    <ellipse role="img" aria-label="faint orca silhouette" cx="95" cy="210" rx="70" ry="26" fill="#1f1b4f" opacity="0.6"/>
    <ellipse role="img" aria-label="faint salmon silhouette" cx="505" cy="188" rx="62" ry="22" fill="#1f1b4f" opacity="0.6"/>
  </svg>
  <div class="brand-seal">LW Gull<br>Rock Tours</div>
  <p class="website">
    <svg width="13" height="13" viewBox="0 0 14 14" aria-hidden="true">
      <circle cx="7" cy="7" r="6" fill="none" stroke="#00a9c5" stroke-width="1.6"/>
      <ellipse cx="7" cy="7" rx="2.6" ry="6" fill="none" stroke="#00a9c5" stroke-width="1.2"/>
      <line x1="1" y1="7" x2="13" y2="7" stroke="#00a9c5" stroke-width="1.2"/>
    </svg>
    lwgullrocktours.com
  </p>
</section>

<section class="card card--back">
  <svg class="card__art" viewBox="0 0 615 351">
    <defs>
      <linearGradient id="photoTone" x1="0" y1="0" x2="1" y2="1">
        <stop offset="0" stop-color="#7a78b8"/>
        <stop offset="0.55" stop-color="#5552a0"/>
        <stop offset="1" stop-color="#3f3c86"/>
      </linearGradient>
    </defs>
    <polygon role="img" aria-label="Photo of a guide on a boat holding a large salmon" points="0,0 615,0 615,351" fill="url(#photoTone)"/>
    <polygon points="0,0 186,106 0,175" fill="var(--teal)"/>
  </svg>
  <div class="brand-seal">LW Gull<br>Rock Tours</div>
  <h1 class="person-name">Ray Shea</h1>
  <ul class="contact-list">
    <li>
      <svg viewBox="0 0 15 17" aria-hidden="true"><rect x="3.5" y="1" width="8" height="15" rx="1.5" fill="none" stroke="#00a9c5" stroke-width="1.8"/><circle cx="7.5" cy="13" r="1" fill="#00a9c5"/></svg>
      250-318-7262
    </li>
    <li>
      <svg viewBox="0 0 15 17" aria-hidden="true"><rect x="0.5" y="4" width="14" height="10" fill="#00a9c5"/><polyline points="0.5,4.5 7.5,10 14.5,4.5" fill="none" stroke="#fff" stroke-width="1.2"/></svg>
      info@lwgullrocktours.com
    </li>
    <li>
      <svg viewBox="0 0 15 17" aria-hidden="true"><path d="M7.5 16 C3 10.5 1.5 8 1.5 6 A6 6 0 0 1 13.5 6 C13.5 8 12 10.5 7.5 16Z" fill="#00a9c5"/><circle cx="7.5" cy="6" r="2.2" fill="#fff"/></svg>
      Campbell River BC
    </li>
  </ul>
</section>

</body>
</html>
```